Vell Brook Perks Needs a Website Design

We need a website design for a new service we are starting. Users enter a coupon in a redemption page and either create an account or sign in. they can then use the credits they accumulate from the coupons to purchase items listed on the site.

we need a design for the following:
-the coupon redemption page (with a choice to either sign in or create an account)
-a product listing page (with search filters and a search bar. the search bar can be displayed in the header of the site)
-a product detail page, showing the product's title, image, credit redemption value, brand and any category associated with the item
-a my account page, with:
*a list of the pluses (coupons/credit added to account) and the minuses (orders placed/credits subtracted from account) to show a detailed description of their history on the site)
*an area for users to edit their name, phone number, address etc
*an area for users to add / edit their casino membership number and casino
*an area for users to add a coupon to their account
-a cart / checkout process:
*cart displaying items and their total
*entering / selecting an address from their account
*review order details page where they can submit their order (and warning the user that doing so will subtract the required credits from their account)

remember that no ecommerce or money is used on the site.. users are spending their credits and checkout their cart with the credits they accumulated, so the items each have a credit redemption value and the checkout process is shown in credits.

we are not very particular with any design preference, other than we'd like it to be predominately white.

If designing the site with css please make sure to use bootstrap in your designs. thanks!

Target Market(s)

adults 45-65

Industry/Entity Type

Casino

Coding

Coded - Design and coding required

Number of Pages Required

5+ page

Font styles to use
Sans Serif

Requirements
Must have
• css must use with bootstrap
Nice to have
• simplified, easy interface. we are targeting an older crowd and dont want to confuse them
Should not have
• the site shouldnt have any dollar values. all product prices, checkout totals and user accrual's (in the my account page) should be in credits

```html
<!DOCTYPE html>
<html lang="en">
<head>
<meta charset="utf-8">
<title>Vell Brook Perks – Coupon Redemption</title>
<link href="https://fonts.googleapis.com/css2?family=Open+Sans:ital,wght@0,400;0,600;0,700;1,700&display=swap" rel="stylesheet">
<style>
  :root{
    --blue:#1a64cc;
    --green:#84b515;
    --ink:#4a4a4a;
    --muted:#666;
    --line:#d6d6d6;
    --footer:#404040;
    --footer-base:#2f2f2f;
    --footer-text:#d9d9d9;
    --white:#fff;
  }
  *{box-sizing:border-box;margin:0;padding:0}
  html,body{width:1200px;height:894px;overflow:hidden;background:var(--white);font-family:"Open Sans",Arial,sans-serif;color:var(--ink)}
  .page{position:relative;width:1200px;height:894px}
  a{text-decoration:none;color:inherit}

  /* Header */
  .brand{position:absolute;left:75px;top:32px;font-size:30px;font-weight:700;color:var(--blue);letter-spacing:.5px}
  .search{position:absolute;left:378px;top:28px;width:458px;height:45px;border:1px solid var(--line);display:flex}
  .search__filter{width:110px;border-right:1px solid var(--line);display:flex;align-items:center;justify-content:center;gap:8px;font-size:15px;color:#555}
  .search__input{flex:1;display:flex;align-items:center;padding-left:14px;font-size:15px;color:#888}
  .search__btn{width:46px;margin:-1px -1px -1px 0;background:var(--blue);display:flex;align-items:center;justify-content:center}
  .account-btn{position:absolute;left:895px;top:14px;width:102px;height:32px;background:var(--green);color:var(--white);font-size:15px;font-weight:700;display:flex;align-items:center;justify-content:center}
  .cart{position:absolute;left:1023px;top:20px;font-size:15px;font-weight:700;color:var(--blue);display:flex;align-items:center;gap:8px}
  .cart__count{color:var(--green);margin-left:4px}
  .nav{position:absolute;top:62px;font-size:15px;font-weight:600;color:var(--muted);letter-spacing:.3px}
  .nav--coupon{left:885px}
  .nav--products{left:1064px}
  .divider{position:absolute;left:75px;top:100px;width:1051px;border-top:1px solid var(--line)}

  /* Redemption form */
  .title{position:absolute;left:0;top:134px;width:1200px;text-align:center;font-size:28px;font-weight:600;color:var(--ink);letter-spacing:.5px}
  .field{position:absolute;width:241px;height:45px;border:1px solid var(--line);padding-left:15px;display:flex;align-items:center;font-size:14px;color:#555}
  .btn{position:absolute;left:435px;width:332px;height:49px;color:var(--white);font-size:18px;font-weight:700;display:flex;align-items:center;justify-content:center;letter-spacing:.5px}
  .btn--submit{top:342px;background:var(--green)}
  .btn--signin{top:434px;background:var(--blue)}
  .or{position:absolute;left:0;top:402px;width:1200px;text-align:center;font-size:17px;font-weight:700;font-style:italic;color:#333}

  /* Footer */
  .footer{position:absolute;left:0;top:566px;width:1200px;height:238px;background:var(--footer);color:var(--footer-text)}
  .footer__col{position:absolute;top:40px}
  .footer__heading{font-size:18px;font-weight:700;color:var(--white);letter-spacing:.5px;margin-bottom:12px}
  .footer__text{font-size:15px;line-height:26px;width:330px}
  .footer__more{display:block;margin-top:7px;font-size:15px;font-weight:700;color:var(--green)}
  .footer__links{list-style:none;font-size:15px;line-height:33px;margin-top:-3px}
  .newsletter__input{width:242px;height:43px;background:var(--white);color:#666;font-size:13px;display:flex;align-items:center;padding-left:14px}
  .newsletter__btn{margin:10px 0 0 152px;width:101px;height:36px;background:var(--green);color:var(--white);font-size:15px;font-weight:700;display:flex;align-items:center;justify-content:center}
  .base{position:absolute;left:0;top:804px;width:1200px;height:90px;background:var(--footer-base)}
  .base__copy{position:absolute;left:76px;top:40px;font-size:13px;color:#bdbdbd}
  .base__social{position:absolute;left:918px;top:836px;display:flex;gap:17px}
  .base__social span{width:22px;height:22px;border-radius:50%;background:#8a8a8a;display:block}
</style>
</head>
<body>
<div class="page">
  <header>
    <div class="brand">Vell Brook Perks</div>
    <div class="search">
      <div class="search__filter">
        <svg width="12" height="12" viewBox="0 0 12 12"><path d="M0 0h12L7.5 5.5V12L4.5 10V5.5z" fill="#555"/></svg>
        Filter
        <svg width="10" height="6" viewBox="0 0 10 6" style="margin-left:10px"><path d="M1 1l4 4 4-4" stroke="#555" stroke-width="1.5" fill="none"/></svg>
      </div>
      <div class="search__input">Search..</div>
      <div class="search__btn">
        <svg width="15" height="15" viewBox="0 0 15 15"><circle cx="6" cy="6" r="4.5" stroke="#fff" stroke-width="2" fill="none"/><path d="M9.5 9.5l4 4" stroke="#fff" stroke-width="2.4" stroke-linecap="round"/></svg>
      </div>
    </div>
    <a class="account-btn" href="#">My Account</a>
    <a class="cart" href="#">
      <svg width="15" height="13" viewBox="0 0 15 13"><path d="M0 1h2.5l2 7h8l2-5.5H4" fill="none" stroke="#1a64cc" stroke-width="1.8"/><path d="M4.5 3h9.5l-1.8 5H5.5z" fill="#1a64cc"/><circle cx="6" cy="11.5" r="1.3" fill="#1a64cc"/><circle cx="11.5" cy="11.5" r="1.3" fill="#1a64cc"/></svg>
      <span>My Cart <span class="cart__count">(0)</span></span>
    </a>
    <a class="nav nav--coupon" href="#">Coupon Redemption</a>
    <a class="nav nav--products" href="#">Products</a>
    <div class="divider"></div>
  </header>

  <main>
    <h1 class="title">Coupon Redemption</h1>
    <div class="field" style="left:210px;top:202px">First Name</div>
    <div class="field" style="left:480px;top:202px">Last Name</div>
    <div class="field" style="left:750px;top:202px">Email Address</div>
    <div class="field" style="left:210px;top:259px">Enter Password</div>
    <div class="field" style="left:480px;top:259px">Re- Enter Password</div>
    <div class="field" style="left:750px;top:259px">Enter Coupon Code</div>
    <a class="btn btn--submit" href="#">Submit Now</a>
    <div class="or">Or</div>
    <a class="btn btn--signin" href="#">Sign In</a>
  </main>

  <footer>
    <div class="footer">
      <div class="footer__col" style="left:76px">
        <h3 class="footer__heading">ABOUT US</h3>
        <p class="footer__text">Aliquam molestie, mi et imperdiet euismod, dui purus auctor tellus, et interdum lacus lectus et ante. Sed accumsan sollicitudin sapien, sit amet adipiscing turpis gravida ac.</p>
        <a class="footer__more" href="#">Read More</a>
      </div>
      <div class="footer__col" style="left:445px">
        <h3 class="footer__heading">POLICIES</h3>
        <ul class="footer__links"><li>Privacy Policy</li><li>User Account</li><li>Shipment</li><li>Terms and Conditions</li></ul>
      </div>
      <div class="footer__col" style="left:688px">
        <h3 class="footer__heading">QUICK LINKS</h3>
        <ul class="footer__links"><li>Contact Us</li><li>About Us</li><li>Careers</li><li>FAQs</li></ul>
      </div>
      <div class="footer__col" style="left:884px">
        <h3 class="footer__heading">SIGN UP NEWSLETTER</h3>
        <div class="newsletter__input">Enter Mail Address</div>
        <a class="newsletter__btn" href="#">Sign Up</a>
      </div>
    </div>
    <div class="base">
      <p class="base__copy">Copyright © 2017. Company Name. All Right Reserved</p>
    </div>
    <div class="base__social" aria-label="Social links"><span></span><span></span><span></span><span></span><span></span><span></span></div>
  </footer>
</div>
</body>
</html>
```